Bellwyn Strategic

Business Development Consulting Firm

Target Market(s)

Federal Government, 8(a) companies, Small Businesses

Industry/Entity Type

Private Sector, US Government

Contact Information for Business Card

8(a) Program Capture, Business Development, Industry Trends & Analysis, Strategic Teaming, Cyber Solutions

Colors

Designer to choose colors to be used in the design.

```html
<!DOCTYPE html>
<html lang="en">
<head>
<meta charset="UTF-8">
<title>Bellwyn Strategic – Business Card</title>
<link href="https://fonts.googleapis.com/css2?family=Roboto:wght@400;500;700&display=swap" rel="stylesheet">
<style>
  :root {
    --navy: #0f2a5c;
    --navy-text: #1d3766;
    --grey-text: #6f6f72;
    --rule: #8a8a8d;
    --paper: #f7f7f5;
    --backdrop: #9a9a9a;
    --white: #ffffff;
  }
  * { margin: 0; padding: 0; box-sizing: border-box; }
  html, body {
    width: 1200px; height: 972px; overflow: hidden;
    background: var(--backdrop);
    font-family: "Roboto", Arial, sans-serif;
  }
  .sheet {
    width: 1200px; height: 972px;
    display: flex; flex-direction: column; align-items: center; justify-content: center;
    gap: 56px;
  }
  .card {
    width: 700px; height: 400px;
    position: relative;
    box-shadow: 0 14px 30px rgba(0,0,0,0.25);
  }
  .card--front { background: var(--paper); }
  .card--back { background: var(--navy); }

  /* front */
  .brand {
    position: absolute; left: 70px; top: 148px;
    display: flex; align-items: center; gap: 16px;
  }
  .brand__mark { width: 26px; height: 26px; border-radius: 50%; background: var(--navy-text); }
  .brand__name {
    font-weight: 500; font-size: 30px; line-height: 1.15; letter-spacing: 3px;
    color: var(--navy-text); text-transform: uppercase;
  }
  .divider {
    position: absolute; left: 382px; top: 95px; width: 1px; height: 210px;
    background: var(--rule);
  }
  .contact { position: absolute; left: 412px; top: 100px; color: var(--grey-text); }
  .contact__name {
    font-weight: 700; font-size: 20px; letter-spacing: 1px; color: var(--navy-text);
    text-transform: uppercase;
  }
  .contact__title { font-size: 15px; margin-top: 2px; }
  .contact__address { font-size: 17px; line-height: 1.3; margin-top: 14px; }
  .contact__list { list-style: none; margin-top: 10px; font-size: 17px; line-height: 1.55; }
  .contact__list li { display: flex; align-items: center; gap: 9px; }
  .contact__list svg { width: 16px; height: 16px; flex: none; }

  /* back */
  .back-brand {
    position: absolute; left: 0; right: 0; top: 130px;
    display: flex; align-items: center; justify-content: center; gap: 20px;
  }
  .back-brand__mark { width: 34px; height: 34px; border-radius: 50%; background: var(--white); }
  .back-brand__name {
    font-weight: 500; font-size: 42px; line-height: 1.15; letter-spacing: 5px;
    color: var(--white); text-transform: uppercase;
  }
  .services {
    position: absolute; left: 0; right: 0; bottom: 70px;
    display: flex; justify-content: center; gap: 14px;
    list-style: none; color: var(--white); font-size: 15.5px; font-weight: 500;
  }
  .services li::before {
    content: ""; display: inline-block; width: 8px; height: 8px; border-radius: 50%;
    background: var(--white); margin-right: 6px; vertical-align: 2px;
  }
</style>
</head>
<body>
<main class="sheet">
  <section class="card card--front" aria-label="Business card front">
    <div class="brand">
      <span class="brand__mark"></span>
      <span class="brand__name">Bellwyn<br>Strategic</span>
    </div>
    <div class="divider"></div>
    <div class="contact">
      <p class="contact__name">Marcus J. Delane</p>
      <p class="contact__title">Founder &amp; CEO</p>
      <p class="contact__address">48 Harbor Lane, Suite 4<br>Milford, CT 06460</p>
      <ul class="contact__list">
        <li>
          <svg viewBox="0 0 24 24" fill="var(--navy-text)" aria-hidden="true"><path d="M6.6 10.8a15.1 15.1 0 0 0 6.6 6.6l2.2-2.2a1 1 0 0 1 1-.25 11.4 11.4 0 0 0 3.6.57 1 1 0 0 1 1 1V20a1 1 0 0 1-1 1A17 17 0 0 1 3 4a1 1 0 0 1 1-1h3.5a1 1 0 0 1 1 1c0 1.25.2 2.45.57 3.6a1 1 0 0 1-.25 1z"/></svg>
          (555) 318-0472
        </li>
        <li>
          <svg viewBox="0 0 24 24" fill="none" stroke="var(--navy-text)" stroke-width="2" aria-hidden="true"><rect x="2" y="5" width="20" height="14"/><path d="M2 5l10 8 10-8"/></svg>
          info@bellwynstrategic.com
        </li>
        <li>
          <svg viewBox="0 0 24 24" fill="none" stroke="var(--navy-text)" stroke-width="1.6" aria-hidden="true"><circle cx="12" cy="12" r="10"/><ellipse cx="12" cy="12" rx="4.5" ry="10"/><path d="M2 12h20M4 7h16M4 17h16"/></svg>
          www.bellwynstrategic.com
        </li>
      </ul>
    </div>
  </section>

  <section class="card card--back" aria-label="Business card back">
    <div class="back-brand">
      <span class="back-brand__mark"></span>
      <span class="back-brand__name">Bellwyn<br>Strategic</span>
    </div>
    <ul class="services">
      <li>Program Capture</li>
      <li>Business Development</li>
      <li>Industry Trends &amp; Analysis</li>
      <li>Strategic Teaming</li>
    </ul>
  </section>
</main>
</body>
</html>
```